Just upload my Logo
Simple
Elsa Marroquín
quillmarshimages@postnook.net
Follow me in Chatterloom
* Wedding
* Engagment
* Maternity
* Newborn
* Family
* Events......etc

```html
<!DOCTYPE html>
<html lang="en">
<head>
<meta charset="utf-8">
<title>Quillmarsh Images – Business Card</title>
<link rel="stylesheet" href="https://fonts.googleapis.com/css2?family=Crimson+Text:wght@400;600&display=swap">
<style>
  :root {
    --backdrop: #d9d9d9;
    --card-white: #ffffff;
    --accent-pink: #ec3f96;
    --band-charcoal: #3c3b3d;
    --ink-dark: #3a3a3a;
    --ink-light: #f2f2f2;
    --divider: #cfcfcf;
  }
  html, body {
    margin: 0;
    padding: 0;
    width: 1200px;
    height: 1050px;
    overflow: hidden;
    background: var(--backdrop);
  }
  .canvas {
    position: relative;
    width: 1200px;
    height: 1050px;
  }
  .business-card {
    position: absolute;
    left: 100px;
    top: 239px;
    width: 1000px;
    height: 572px;
    border-radius: 30px;
    overflow: hidden;
    background: var(--card-white);
    box-shadow: 0 10px 30px rgba(0,0,0,0.18);
  }
  .card-bands {
    position: absolute;
    inset: 0;
    width: 1000px;
    height: 572px;
  }
  .band-pink { fill: var(--accent-pink); }
  .band-charcoal { fill: var(--band-charcoal); }
  .brand-mark {
    position: absolute;
    left: 220px;
    top: 100px;
    display: flex;
    align-items: center;
    gap: 22px;
  }
  .brand-dot {
    width: 26px;
    height: 26px;
    border-radius: 50%;
    background: var(--accent-pink);
  }
  .brand-name {
    font-family: "Crimson Text", serif;
    font-weight: 400;
    font-size: 64px;
    letter-spacing: 1px;
    color: var(--ink-dark);
    line-height: 1;
  }
  .service-list {
    position: absolute;
    left: 268px;
    top: 190px;
    margin: 0;
    padding: 0;
    list-style: none;
    display: flex;
    gap: 10px;
    font-family: "Crimson Text", serif;
    font-weight: 400;
    font-size: 19px;
    letter-spacing: 1px;
    text-transform: uppercase;
    color: var(--accent-pink);
  }
  .service-item + .service-item::before {
    content: "·";
    margin-right: 10px;
    color: var(--ink-dark);
  }
  .holder-name {
    position: absolute;
    left: 62px;
    top: 448px;
    font-family: "Crimson Text", serif;
    font-weight: 600;
    font-size: 38px;
    color: var(--ink-light);
  }
  .contact-divider {
    position: absolute;
    left: 398px;
    top: 392px;
    width: 2px;
    height: 126px;
    background: var(--divider);
  }
  .contact-list {
    position: absolute;
    left: 422px;
    top: 394px;
    margin: 0;
    padding: 0;
    list-style: none;
    font-family: "Crimson Text", serif;
    font-size: 24px;
    color: var(--ink-light);
  }
  .contact-item {
    display: flex;
    align-items: center;
    gap: 14px;
    height: 40px;
  }
  .contact-icon {
    width: 20px;
    height: 24px;
    fill: var(--ink-light);
  }
</style>
</head>
<body>
<div class="canvas">
  <div class="business-card">
    <svg class="card-bands" viewBox="0 0 1000 572" aria-hidden="true">
      <path class="band-pink" d="M0 300 C 250 380, 620 330, 1000 238 L1000 572 L0 572 Z"/>
      <path class="band-charcoal" d="M0 335 C 250 412, 620 366, 1000 276 L1000 572 L0 572 Z"/>
    </svg>

    <div class="brand-mark">
      <span class="brand-dot"></span>
      <span class="brand-name">Quillmarsh Images</span>
    </div>

    <ul class="service-list">
      <li class="service-item">Wedding</li>
      <li class="service-item">Engagement</li>
      <li class="service-item">Maternity</li>
      <li class="service-item">Newborn</li>
      <li class="service-item">Family</li>
      <li class="service-item">Events</li>
    </ul>

    <div class="holder-name">Elsa Marroquín</div>
    <div class="contact-divider"></div>

    <ul class="contact-list">
      <li class="contact-item">
        <svg class="contact-icon" viewBox="0 0 20 24" aria-hidden="true">
          <rect x="4" y="1" width="12" height="22" rx="2.5"/>
          <rect x="6.5" y="4" width="7" height="11" fill="#3c3b3d"/>
          <circle cx="10" cy="19" r="1.5" fill="#3c3b3d"/>
        </svg>
        <span>(555) 318-0476</span>
      </li>
      <li class="contact-item">
        <svg class="contact-icon" viewBox="0 0 20 24" aria-hidden="true">
          <text x="10" y="19" text-anchor="middle" font-family="Crimson Text, serif" font-size="22" fill="#f2f2f2">@</text>
        </svg>
        <span>quillmarshimages@postnook.net</span>
      </li>
      <li class="contact-item">
        <svg class="contact-icon" viewBox="0 0 20 24" aria-hidden="true">
          <circle cx="10" cy="12" r="6"/>
        </svg>
        <span>Follow me in Chatterloom</span>
      </li>
    </ul>
  </div>
</div>
</body>
</html>
```